Industry leading Property Management Company needs a flyer!

We need a brochure describing our fees and a basic description of what we do. This brochure will be printed, to be given to prospective clients, but we would also like an electronic version that can be downloaded from our website as a PDF. This project will be printed double sided, on standard 8.5" x 11" paper, in landscape mode, as a tri-fold brochure.

Target Market(s)

Real estate investors, but more importantly, first time investors. Many of our clients are "accidental landlords" who had their property for sale that didn't sell, so they are trying property management and rental investing for the first time. TRUST is their biggest fear

Font styles to use
Sans Serif

Requirements
Must have
• Must incorporate our logo, elements of our pricing list, and incorporate the text from our home page and "property management info" page (www.corvalinkrent.net). A word document specifying this text has been included in the project brief.
• Additionally, I am thinking this will be a simple, single piece of paper, in landscape mode, printed on both sides, in a Tri-fold. The front of the brochure will have the logo/name of the company, along with the Harbor Tenant Medals logos. I am thinking the first inside pane, when someone opens up the brochure, will have reference text #1 and #3. The 3 tiered pricing plan might occupy the 2nd and 3rd of the three panes on the inside fold. Reference text #4, 5, and 6 will occupy the next pane (see brief for handwritten layout). Then, the very back pane (when it is folded and shut) will have reference text #2 and our company contact information, plus any kind of stock photos, etc.
Nice to have
• Our main market will be first time investors, so we need to display and demonstrate relationships, and trust. We would prefer stock photos that incorporate families, children, or other images that solidify peace of mind.

```html
<!DOCTYPE html>
<html lang="en">
<head>
<meta charset="utf-8">
<title>Corvalink Rent Management – Tri-fold Brochure</title>
<link href="https://fonts.googleapis.com/css2?family=Open+Sans:wght@400;600;700;800&family=Montserrat:wght@600;700;800&display=swap" rel="stylesheet">
<style>
:root{
  --blue:#1f80c6;
  --blue-dark:#135e9a;
  --navy:#1d2733;
  --ink:#3b4550;
  --muted:#7a848e;
  --rule:#d9dee3;
  --paper:#ffffff;
  --stage:#f1f2f4;
  --gold:#c89a2c;
  --red:#b8312f;
}
*{box-sizing:border-box;margin:0;padding:0}
html,body{width:800px;height:1200px;overflow:hidden;background:var(--stage)}
body{font-family:"Open Sans",Arial,sans-serif;color:var(--ink);position:relative}
.sheet{position:absolute;left:40px;width:720px;height:556px;background:var(--paper);box-shadow:0 2px 8px rgba(0,0,0,.18);overflow:hidden}
.sheet-outside{top:30px}
.sheet-inside{top:614px}
.panel{position:absolute;top:0;height:556px;width:240px}
.p1{left:0}.p2{left:240px}.p3{left:480px}
.pad{padding:22px 20px}
h3.section-title{font-family:"Montserrat",sans-serif;font-size:9px;font-weight:800;color:var(--blue);letter-spacing:.5px;text-transform:uppercase;margin:10px 0 5px}
h3.section-title:first-child{margin-top:0}
p.body{font-size:6.2px;line-height:1.55;margin-bottom:5px;color:var(--ink)}
ul.bullets{list-style:none;margin:4px 0 6px}
ul.bullets li{font-size:6.2px;line-height:1.6;padding-left:8px;position:relative}
ul.bullets li::before{content:"";position:absolute;left:0;top:3px;width:3px;height:3px;background:var(--blue)}
.photo{position:absolute;background:linear-gradient(135deg,#c9b79c 0%,#8f7a62 45%,#4f5d6b 100%)}
.photo.bright{background:linear-gradient(135deg,#e6d8c3 0%,#b7a084 50%,#6d7d8c 100%)}
.shape{position:absolute;left:0;top:0}
.why-title{font-family:"Montserrat",sans-serif;font-size:10.5px;font-weight:700;color:var(--navy);line-height:1.3;margin-bottom:6px}
.badges{display:flex;gap:14px;justify-content:center;margin:8px 0 10px}
.badge{width:42px;height:42px;border-radius:50%;background:radial-gradient(circle,var(--gold) 0 55%,var(--red) 56% 100%)}
.tollfree{font-family:"Montserrat",sans-serif;font-size:11px;font-weight:800;color:var(--blue);text-align:center;margin-bottom:6px}
.contact-line{font-size:6px;color:var(--ink);text-align:center;display:flex;justify-content:center;gap:10px;align-items:center}
.contact-line svg{vertical-align:middle;margin-right:2px}
.footer-bar{position:absolute;left:0;bottom:0;width:100%;height:26px;background:var(--navy)}
.brand{position:absolute;left:0;top:0;width:240px;height:80px;display:flex;align-items:center;justify-content:center;gap:7px}
.brand-mark{width:14px;height:14px;background:var(--blue)}
.brand-name{font-family:"Montserrat",sans-serif;font-weight:800;font-size:13px;color:var(--navy);letter-spacing:.5px;line-height:1.05;text-transform:uppercase}
.cover-band{position:absolute;left:0;top:380px;width:240px;height:110px;background:var(--navy);padding:22px 20px;text-align:center}
.cover-band .kicker{font-size:7px;font-weight:700;color:#fff;letter-spacing:.6px;text-transform:uppercase;line-height:1.5}
.cover-band .headline{font-family:"Montserrat",sans-serif;font-size:13px;font-weight:800;color:#fff;text-transform:uppercase;line-height:1.25;margin-top:6px}
.cover-band .headline span{color:#6fb8ea}
.web{position:absolute;left:0;bottom:22px;width:240px;text-align:center;font-family:"Montserrat",sans-serif;font-size:8px;font-weight:700;color:var(--navy);letter-spacing:1.5px}
.web.on-dark{bottom:8px;color:#fff;font-size:7px}
.service{display:flex;gap:8px;margin-bottom:7px}
.service-icon{flex:0 0 22px;height:22px;background:var(--navy);display:flex;align-items:center;justify-content:center}
.service h4{font-size:7px;font-weight:700;color:var(--blue);margin-bottom:1px}
.service p{font-size:5.8px;line-height:1.5}
.pricing{position:absolute;left:240px;top:0;width:480px;height:556px;padding:20px 22px}
.pricing-title{font-family:"Montserrat",sans-serif;font-size:10px;font-weight:800;color:var(--blue);text-transform:uppercase}
.pricing-sub{font-size:6px;color:var(--muted);margin-bottom:6px}
.popular{position:absolute;right:22px;top:20px;width:240px;height:20px;background:#e9edf1;font-family:"Montserrat",sans-serif;font-weight:800;font-size:9px;color:var(--navy);text-align:center;line-height:20px;letter-spacing:1px}
table.plans{width:100%;border-collapse:collapse;margin-top:12px}
table.plans th{background:var(--blue);color:#fff;font-size:6px;font-weight:700;padding:5px 3px;border:1px solid #fff;text-align:center;line-height:1.3;vertical-align:top}
table.plans th.feature{background:transparent}
table.plans th .price{display:block;font-size:5.4px;font-weight:400;margin-top:3px}
table.plans th.mid{background:var(--blue-dark)}
table.plans td{font-size:5.8px;padding:2.6px 5px;border-bottom:1px solid var(--rule);height:13.4px}
table.plans td.cell{text-align:center;width:80px;border-left:1px solid var(--rule)}
table.plans tr:nth-child(even) td{background:#f5f7f9}
.tick{display:inline-block;width:3.5px;height:6px;border-right:1.5px solid var(--navy);border-bottom:1.5px solid var(--navy);transform:rotate(45deg)}
.note{font-size:5.4px;color:var(--muted);margin-top:6px;line-height:1.5}
</style>
</head>
<body>

<!-- OUTSIDE OF BROCHURE -->
<section class="sheet sheet-outside">
  <div class="panel p1 pad">
    <h3 class="section-title">Our Purpose</h3>
    <p class="body">Corvalink Rent Management was founded to take the stress out of owning a rental home. We treat every property as if it were our own, giving owners clear reports, steady income and honest advice at every step.</p>
    <p class="body">Many of our owners never planned to be landlords. Whether your home did not sell or you are buying your first investment, our team guides you from listing to lease and beyond.</p>
    <p class="body">We combine local market knowledge with modern tools so owners always know what is happening with their homes, their tenants and their money.</p>
    <h3 class="section-title">Tenant Happiness And Retention</h3>
    <p class="body">Happy tenants stay longer, care for the home and pay on time. We respond quickly to requests and keep open lines of communication.</p>
    <p class="body">We make it easy for tenants to reach us, any day of the week:</p>
    <ul class="bullets">
      <li>Online rent payment portal</li>
      <li>Maintenance requests 24/7</li>
      <li>Friendly, local office staff</li>
      <li>Clear lease renewal process</li>
    </ul>
    <p class="body">Lower turnover means fewer vacant months, lower make-ready costs and a steadier return for you as the owner.</p>
    <h3 class="section-title">Transparency And Reporting</h3>
    <p class="body">Owners receive monthly statements, year-end tax summaries and photos from every inspection through a secure online account.</p>
    <p class="body">Every expense is itemized and every repair is explained, so you can make decisions with full confidence in the numbers.</p>
  </div>

  <div class="panel p2">
    <div class="photo bright" role="img" aria-label="Photo of a smiling family relaxing together at home" style="left:0;top:0;width:240px;height:160px"></div>
    <svg class="shape" width="240" height="180" viewBox="0 0 240 180" aria-hidden="true">
      <polygon points="0,120 240,150 240,180 0,180" fill="#ffffff"/>
      <polygon points="0,112 150,130 0,148" fill="var(--blue)"/>
    </svg>
    <div class="pad" style="position:absolute;top:170px;left:0;width:240px;padding-top:0">
      <div class="why-title">Why choose Corvalink Rent as your property management company</div>
      <p class="body">Our licensed managers, local maintenance partners and transparent pricing give owners peace of mind. We screen every applicant, protect your home and keep your investment earning.</p>
      <p class="body">Our work has been recognized by the Harbor Tenant Medals for outstanding service to owners and residents.</p>
      <div class="badges">
        <div class="badge"></div>
        <div class="badge"></div>
      </div>
      <div class="tollfree">Toll Free: 1-800-555-0142</div>
      <div class="contact-line">
        <span><svg width="7" height="7" viewBox="0 0 10 10"><path d="M2 1l2 2-1 1.5c.6 1.3 1.5 2.2 2.5 2.5L7 6l2 2-1.5 1.5C4.5 9 1 5.5.5 2.5z" fill="var(--blue)"/></svg>1-800-555-0142</span>
        <span><svg width="8" height="6" viewBox="0 0 10 8"><rect x=".5" y=".5" width="9" height="7" fill="none" stroke="var(--blue)"/><path d="M.5.5l4.5 4 4.5-4" fill="none" stroke="var(--blue)"/></svg>hello@corvalinkrent.net</span>
      </div>
      <div class="contact-line" style="margin-top:4px">
        <span><svg width="6" height="8" viewBox="0 0 6 8"><path d="M3 0a3 3 0 0 1 3 3c0 2-3 5-3 5S0 5 0 3a3 3 0 0 1 3-3z" fill="var(--blue)"/></svg>214 Harbor Point Way, Suite 9, Bayfield</span>
      </div>
    </div>
    <div class="footer-bar"></div>
  </div>

  <div class="panel p3">
    <div class="brand">
      <span class="brand-mark"></span>
      <span class="brand-name">Corvalink Rent<br>Management</span>
    </div>
    <div class="photo" role="img" aria-label="Photo of a family with children enjoying time in front of their home" style="left:0;top:80px;width:240px;height:300px"></div>
    <svg class="shape" width="240" height="380" viewBox="0 0 240 380" aria-hidden="true">
      <polygon points="0,80 90,80 0,150" fill="var(--blue)"/>
      <polygon points="240,300 240,380 130,380" fill="var(--blue)"/>
      <polygon points="240,340 240,380 180,380" fill="var(--navy)"/>
    </svg>
    <div class="cover-band">
      <div class="kicker">Corvalink Rent Management offer the</div>
      <div class="headline">World Class <span>Management Services</span></div>
    </div>
    <div class="web">www.corvalinkrent.net</div>
  </div>
</section>

<!-- INSIDE OF BROCHURE -->
<section class="sheet sheet-inside">
  <div class="panel p1 pad">
    <h3 class="section-title">About Us</h3>
    <p class="body">Corvalink Rent Management is a full service residential management company serving single family homes, condos and small multi-unit buildings across the region.</p>
    <p class="body">Our team has helped hundreds of first-time owners turn an unsold home into a reliable rental, with honest guidance and no hidden fees.</p>
    <h3 class="section-title">Our Services</h3>
    <p class="body">Every plan includes the essentials an owner needs to rent with confidence.</p>
    <div class="service">
      <div class="service-icon"><svg width="12" height="12" viewBox="0 0 12 12"><path d="M1 6l5-4.5L11 6v5H7V8H5v3H1z" fill="#fff"/></svg></div>
      <div><h4>Property Management</h4><p>Day to day care of your home, tenants and rent collection.</p></div>
    </div>
    <div class="service">
      <div class="service-icon"><svg width="12" height="12" viewBox="0 0 12 12"><circle cx="5" cy="5" r="3.5" fill="none" stroke="#fff" stroke-width="1.5"/><path d="M7.5 7.5L11 11" stroke="#fff" stroke-width="1.5"/></svg></div>
      <div><h4>Tenant Screening</h4><p>Credit, income, rental history and background checks.</p></div>
    </div>
    <div class="service">
      <div class="service-icon"><svg width="12" height="12" viewBox="0 0 12 12"><path d="M2 10l5-5M7 2a3 3 0 0 0 3 3" stroke="#fff" stroke-width="1.6" fill="none"/></svg></div>
      <div><h4>Property Maintenance</h4><p>Vetted local vendors and fair pricing on every repair.</p></div>
    </div>
    <div class="service">
      <div class="service-icon"><svg width="12" height="12" viewBox="0 0 12 12"><rect x="2" y="1" width="8" height="10" fill="none" stroke="#fff" stroke-width="1.4"/><path d="M4 4h4M4 6h4M4 8h3" stroke="#fff"/></svg></div>
      <div><h4>Owner Reporting</h4><p>Monthly statements and year-end tax summaries online.</p></div>
    </div>
    <div class="service">
      <div class="service-icon"><svg width="12" height="12" viewBox="0 0 12 12"><path d="M2 6.5l2.5 2.5L10 3" stroke="#fff" stroke-width="1.6" fill="none"/></svg></div>
      <div><h4>Leasing &amp; Marketing</h4><p>Photos, listings and showings to fill vacancies fast.</p></div>
    </div>
    <div class="footer-bar"></div>
    <div class="web on-dark">www.corvalinkrent.net</div>
  </div>

  <div class="pricing">
    <div class="pricing-title">Pricing</div>
    <div class="pricing-sub">Simple plans for every owner</div>
    <div class="popular">MOST POPULAR</div>
    <table class="plans">
      <thead>
        <tr>
          <th class="feature"></th>
          <th>Basic Plan<span class="price">8% of monthly rent</span></th>
          <th class="mid">Premium Plan<span class="price">10% of monthly rent</span></th>
          <th>Elite Plan<span class="price">12% of monthly rent</span></th>
        </tr>
      </thead>
      <tbody>
        <tr><td>Rent collection &amp; deposit</td><td class="cell"><span class="tick"></span></td><td class="cell"><span class="tick"></span></td><td class="cell"><span class="tick"></span></td></tr>
        <tr><td>Online owner portal</td><td class="cell"><span class="tick"></span></td><td class="cell"><span class="tick"></span></td><td class="cell"><span class="tick"></span></td></tr>
        <tr><td>Monthly owner statements</td><td class="cell"><span class="tick"></span></td><td class="cell"><span class="tick"></span></td><td class="cell"><span class="tick"></span></td></tr>
        <tr><td>Year-end tax summary</td><td class="cell"><span class="tick"></span></td><td class="cell"><span class="tick"></span></td><td class="cell"><span class="tick"></span></td></tr>
        <tr><td>Tenant screening</td><td class="cell"><span class="tick"></span></td><td class="cell"><span class="tick"></span></td><td class="cell"><span class="tick"></span></td></tr>
        <tr><td>Lease preparation &amp; signing</td><td class="cell"><span class="tick"></span></td><td class="cell"><span class="tick"></span></td><td class="cell"><span class="tick"></span></td></tr>
        <tr><td>24/7 maintenance line</td><td class="cell"><span class="tick"></span></td><td class="cell"><span class="tick"></span></td><td class="cell"><span class="tick"></span></td></tr>
        <tr><td>Vendor coordination</td><td class="cell"><span class="tick"></span></td><td class="cell"><span class="tick"></span></td><td class="cell"><span class="tick"></span></td></tr>
        <tr><td>Move-in inspection with photos</td><td class="cell"><span class="tick"></span></td><td class="cell"><span class="tick"></span></td><td class="cell"><span class="tick"></span></td></tr>
        <tr><td>Move-out inspection with photos</td><td class="cell"><span class="tick"></span></td><td class="cell"><span class="tick"></span></td><td class="cell"><span class="tick"></span></td></tr>
        <tr><td>Professional marketing photos</td><td class="cell"></td><td class="cell"><span class="tick"></span></td><td class="cell"><span class="tick"></span></td></tr>
        <tr><td>Listing on major rental sites</td><td class="cell"></td><td class="cell"><span class="tick"></span></td><td class="cell"><span class="tick"></span></td></tr>
        <tr><td>Scheduled showings</td><td class="cell"></td><td class="cell"><span class="tick"></span></td><td class="cell"><span class="tick"></span></td></tr>
        <tr><td>Annual property inspection</td><td class="cell"></td><td class="cell"><span class="tick"></span></td><td class="cell"><span class="tick"></span></td></tr>
        <tr><td>Lease renewal handling</td><td class="cell"></td><td class="cell"><span class="tick"></span></td><td class="cell"><span class="tick"></span></td></tr>
        <tr><td>Rent increase analysis</td><td class="cell"></td><td class="cell"><span class="tick"></span></td><td class="cell"><span class="tick"></span></td></tr>
        <tr><td>Eviction protection</td><td class="cell"></td><td class="cell"></td><td class="cell"><span class="tick"></span></td></tr>
        <tr><td>Legal notice preparation</td><td class="cell"></td><td class="cell"></td><td class="cell"><span class="tick"></span></td></tr>
        <tr><td>Semi-annual inspections</td><td class="cell"></td><td class="cell"></td><td class="cell"><span class="tick"></span></td></tr>
        <tr><td>Rent guarantee program</td><td class="cell"></td><td class="cell"></td><td class="cell"><span class="tick"></span></td></tr>
        <tr><td>Dedicated account manager</td><td class="cell"></td><td class="cell"></td><td class="cell"><span class="tick"></span></td></tr>
        <tr><td>Priority owner support</td><td class="cell"></td><td class="cell"></td><td class="cell"><span class="tick"></span></td></tr>
      </tbody>
    </table>
    <p class="note">Leasing fee of one half month's rent applies to new tenant placements. Lease renewal fee of $150 on Basic plan only. All plans can be cancelled with 30 days written notice.</p>
  </div>
  <svg class="shape" style="left:240px;top:506px" width="480" height="50" viewBox="0 0 480 50" aria-hidden="true">
    <polygon points="0,24 480,10 480,50 0,50" fill="var(--navy)"/>
    <polygon points="300,15 480,10 480,22" fill="var(--blue)"/>
  </svg>
</section>

</body>
</html>
```